VORL Feature Icons

We have existing feature icons we would like to redesign.
See existing icons at http://www.vorltechnik.example/vorl-platform. Single color icons are prefered, flat design.

I would also like a new "wrapper" icon for our agents and plugins. We currently use a "circle" icon with different graphics inside representing different tech. I would like another take on the "circle" and still be able to use tech graphic inside. See existing wrapper icon at http://www.vorltechnik.example/vorl-plugins

Target Market(s)

Enterprise, B2B

Requirements
Must have
• Colors should fit existing palette on the website

```html
<!DOCTYPE html>
<html lang="en">
<head>
<meta charset="utf-8">
<title>VORL Feature Icons</title>
<link href="https://fonts.googleapis.com/css2?family=Source+Sans+3:wght@400;600&display=swap" rel="stylesheet">
<style>
:root{
  --disc:#1a87c9;
  --disc-shadow:#1d5f8e;
  --disc-deep:#1f6596;
  --ring:#1f6596;
  --accent:#f5a623;
  --ink:#1e1e1e;
  --frame:#8a8a8a;
  --paper:#ffffff;
  --glyph:#ffffff;
}
*{box-sizing:border-box;margin:0;padding:0}
html,body{width:1195px;height:1200px;overflow:hidden;background:var(--paper)}
body{font-family:"Source Sans 3",sans-serif;color:var(--ink);position:relative}
.canvas{position:absolute;inset:0;border:1px solid var(--frame)}
.panel{position:absolute;border:1px solid var(--frame)}
.panel--features{left:20px;top:16px;width:1164px;height:551px}
.panel--agents{left:164px;top:579px;width:837px;height:303px}
.panel--plugins{left:165px;top:897px;width:837px;height:290px}
.feature{position:absolute;width:190px;text-align:center}
.feature svg{display:block;width:110px;height:110px;margin:0 auto}
.feature p{margin-top:14px;font-size:15px;line-height:19px;white-space:nowrap}
.section-title{position:absolute;left:0;right:0;text-align:center;font-size:19px;font-weight:400;letter-spacing:.2px}
.badge{position:absolute;width:110px;height:110px}
.badge--ringed{width:126px;height:126px}
.badge svg{width:100%;height:100%;display:block}
.badge text{font-family:"Source Sans 3",sans-serif;fill:var(--glyph);font-weight:400}
.disc{fill:var(--disc)}
.disc-deep{fill:var(--disc-deep)}
.shade{fill:var(--disc-shadow)}
.g{fill:var(--glyph)}
.gs{fill:none;stroke:var(--glyph);stroke-linecap:round;stroke-linejoin:round}
.gs-blue{fill:none;stroke:var(--disc);stroke-linecap:round;stroke-linejoin:round}
.acc{fill:var(--accent)}
.ring{fill:none;stroke:var(--ring);stroke-width:1.5;stroke-dasharray:2 2.5}
</style>
</head>
<body>
<svg width="0" height="0" style="position:absolute" aria-hidden="true">
  <defs>
    <clipPath id="disc-clip"><circle cx="60" cy="60" r="60"/></clipPath>
  </defs>
</svg>

<div class="canvas">
  <section class="panel panel--features">
    <div class="feature" style="left:-6px;top:34px">
      <svg viewBox="0 0 120 120"><circle class="disc" cx="60" cy="60" r="60"/>
        <polygon class="shade" clip-path="url(#disc-clip)" points="30,55 70,30 140,100 140,140 90,140 35,85"/>
        <circle class="gs" cx="52" cy="66" r="14" stroke-width="9" stroke-dasharray="6 5"/><circle class="g" cx="52" cy="66" r="13"/><circle class="disc" cx="52" cy="66" r="6"/>
        <circle class="gs" cx="78" cy="44" r="9" stroke-width="6" stroke-dasharray="4 3.5"/><circle class="g" cx="78" cy="44" r="8"/><circle class="disc" cx="78" cy="44" r="3.5"/>
      </svg>
      <p>VORL focuses on your<br>integrations.<br>On-premises, cloud<br>and custom</p>
    </div>
    <div class="feature" style="left:186px;top:34px">
      <svg viewBox="0 0 120 120" role="img" aria-label="Machine learning icon"><circle class="disc" cx="60" cy="60" r="60"/>
        <polygon class="shade" clip-path="url(#disc-clip)" points="88,36 140,88 140,140 88,140 34,86"/>
        <g class="gs" stroke-width="3">
          <line x1="40" y1="42" x2="60" y2="60"/><line x1="40" y1="78" x2="60" y2="60"/>
          <line x1="60" y1="60" x2="82" y2="40"/><line x1="60" y1="60" x2="82" y2="60"/><line x1="60" y1="60" x2="82" y2="80"/>
        </g>
        <g class="g"><circle cx="40" cy="42" r="7"/><circle cx="40" cy="78" r="7"/><circle cx="82" cy="40" r="7"/><circle cx="82" cy="60" r="7"/><circle cx="82" cy="80" r="7"/></g>
        <circle class="g" cx="60" cy="60" r="11"/><circle class="disc" cx="60" cy="60" r="5"/>
      </svg>
      <p>Machine learning is<br>used to set dynamic<br>alert thresholds for<br>your integrations</p>
    </div>
    <div class="feature" style="left:377px;top:34px">
      <svg viewBox="0 0 120 120"><circle class="disc" cx="60" cy="60" r="60"/>
        <polygon class="shade" clip-path="url(#disc-clip)" points="35,85 90,35 140,85 140,140 90,140"/>
        <polyline class="gs" stroke-width="5" points="36,36 36,84 88,84"/>
        <polyline class="gs" stroke-width="5" points="42,78 50,52 60,72 70,50 78,62 92,38"/>
        <polygon class="g" points="94,34 82,36 92,46"/>
      </svg>
      <p>Chart and correlate<br>any metric collected<br>from the VORL<br>agents</p>
    </div>
    <div class="feature" style="left:569px;top:34px">
      <svg viewBox="0 0 120 120"><circle class="disc" cx="60" cy="60" r="60"/>
        <polygon class="shade" clip-path="url(#disc-clip)" points="80,35 140,95 140,140 95,140 35,80"/>
        <g class="g"><circle cx="40" cy="40" r="6.5"/><circle cx="60" cy="40" r="6.5"/><circle cx="80" cy="40" r="6.5"/>
        <circle cx="60" cy="60" r="6.5"/><circle cx="80" cy="60" r="6.5"/>
        <circle cx="40" cy="80" r="6.5"/><circle cx="60" cy="80" r="6.5"/><circle cx="80" cy="80" r="6.5"/></g>
        <circle class="acc" cx="40" cy="60" r="6.5"/>
      </svg>
      <p>VORL can detect<br>anomalies at an early<br>stage and alert you</p>
    </div>
    <div class="feature" style="left:760px;top:34px">
      <svg viewBox="0 0 120 120"><circle class="disc" cx="60" cy="60" r="60"/>
        <polygon class="shade" clip-path="url(#disc-clip)" points="62,28 92,58 140,110 140,140 60,140 58,95"/>
        <g class="gs" stroke-width="3"><line x1="32" y1="60" x2="60" y2="30"/><line x1="32" y1="60" x2="90" y2="60"/><line x1="32" y1="60" x2="60" y2="90"/></g>
        <g class="g"><circle cx="32" cy="60" r="7"/><circle cx="60" cy="30" r="7"/><circle cx="90" cy="60" r="7"/><circle cx="60" cy="90" r="7"/></g>
      </svg>
      <p>The Topological map<br>provides insight and<br>process overview</p>
    </div>
    <div class="feature" style="left:952px;top:34px">
      <svg viewBox="0 0 120 120"><circle class="disc" cx="60" cy="60" r="60"/>
        <polygon class="shade" clip-path="url(#disc-clip)" points="88,56 140,108 140,140 84,140 32,90"/>
        <path class="gs" stroke-width="8" d="M46,56 V42 a14,14 0 0 1 28,0 V56"/>
        <rect class="g" x="34" y="54" width="52" height="38" rx="2"/>
        <circle class="disc" cx="60" cy="68" r="5"/><rect class="disc" x="57.5" y="70" width="5" height="12"/>
      </svg>
      <p>Separate runtime and<br>data storage, encrypted<br>connections</p>
    </div>

    <div class="feature" style="left:-6px;top:288px">
      <svg viewBox="0 0 120 120"><circle class="disc" cx="60" cy="60" r="60"/>
        <polygon class="shade" clip-path="url(#disc-clip)" points="70,25 95,45 140,90 140,140 60,140 40,95"/>
        <g transform="rotate(45 75 40)"><rect class="g" x="66" y="22" width="18" height="26" rx="2"/><rect class="g" x="70" y="48" width="10" height="14"/>
        <g class="disc"><rect x="69" y="26" width="2" height="8"/><rect x="73" y="26" width="2" height="8"/><rect x="77" y="26" width="2" height="8"/></g></g>
        <path class="gs" stroke-width="5" d="M58,58 C40,70 34,86 46,92 C54,96 62,94 66,90"/>
      </svg>
      <p>Use the Plugins to<br>push VORL alerts and<br>information to other<br>systems</p>
    </div>
    <div class="feature" style="left:186px;top:288px">
      <svg viewBox="0 0 120 120"><circle class="disc" cx="60" cy="60" r="60"/>
        <polygon class="shade" clip-path="url(#disc-clip)" points="95,50 140,95 140,140 70,140 45,95"/>
        <path class="g" d="M30,66 a12,12 0 0 1 6,-22 a18,18 0 0 1 34,-8 a14,14 0 0 1 20,14 a9,9 0 0 1 0,16 Z"/>
        <rect class="g" x="44" y="44" width="28" height="46" rx="3" stroke="#1a87c9" stroke-width="3"/>
        <g class="gs-blue" stroke-width="2"><line x1="50" y1="52" x2="66" y2="52"/><line x1="50" y1="58" x2="66" y2="58"/><line x1="50" y1="64" x2="66" y2="64"/><line x1="50" y1="70" x2="66" y2="70"/><line x1="50" y1="76" x2="66" y2="76"/></g>
      </svg>
      <p>VORL can be<br>delivered as a cloud<br>service or complete<br>on-premises install</p>
    </div>
    <div class="feature" style="left:377px;top:288px">
      <svg viewBox="0 0 120 120"><circle class="disc" cx="60" cy="60" r="60"/>
        <polygon class="shade" clip-path="url(#disc-clip)" points="80,30 140,90 140,140 60,140 34,110"/>
        <circle class="gs" cx="66" cy="44" r="18" stroke-width="5"/>
        <rect class="g" x="60" y="32" width="12" height="24" rx="1"/>
        <g class="gs-blue" stroke-width="1.5"><line x1="62" y1="37" x2="70" y2="37"/><line x1="62" y1="41" x2="70" y2="41"/><line x1="62" y1="45" x2="70" y2="45"/></g>
        <line class="gs" x1="52" y1="58" x2="34" y2="78" stroke-width="9"/>
      </svg>
      <p>VORL has monitoring<br>agents for integration<br>platforms and<br>peripherals</p>
    </div>
    <div class="feature" style="left:569px;top:288px">
      <svg viewBox="0 0 120 120"><circle class="disc" cx="60" cy="60" r="60"/>
        <polygon class="shade" clip-path="url(#disc-clip)" points="90,35 140,85 140,140 85,140 32,85"/>
        <line class="gs" x1="34" y1="36" x2="84" y2="86" stroke-width="9"/>
        <line class="gs" x1="86" y1="34" x2="36" y2="84" stroke-width="9"/>
        <rect class="g" x="24" y="28" width="24" height="12" transform="rotate(45 36 34)"/>
        <circle class="g" cx="86" cy="34" r="10"/><circle class="disc" cx="90" cy="30" r="5"/>
      </svg>
      <p>VORL has its own SDK<br>so you can create your<br>own custom agents</p>
    </div>
    <div class="feature" style="left:760px;top:288px">
      <svg viewBox="0 0 120 120"><circle class="disc" cx="60" cy="60" r="60"/>
        <polygon class="shade" clip-path="url(#disc-clip)" points="84,32 140,88 140,140 90,140 40,92"/>
        <path class="g" d="M38,24 H72 L84,36 V94 H38 Z"/>
        <rect class="disc" x="43" y="29" width="36" height="60"/>
        <g class="g"><rect x="46" y="34" width="18" height="3"/><rect x="46" y="40" width="18" height="3"/><rect x="46" y="46" width="28" height="3"/>
        <rect x="48" y="70" width="5" height="14"/><rect x="56" y="64" width="5" height="20"/><rect x="64" y="72" width="5" height="12"/><rect x="72" y="62" width="5" height="22"/></g>
        <polyline class="gs" stroke-width="2" points="48,66 56,58 64,62 76,54"/>
      </svg>
      <p>Create reports on any<br>transaction and<br>business metric</p>
    </div>
    <div class="feature" style="left:952px;top:288px">
      <svg viewBox="0 0 120 120"><circle class="disc" cx="60" cy="60" r="60"/>
        <polygon class="shade" clip-path="url(#disc-clip)" points="94,36 140,82 140,140 80,140 30,90 30,84"/>
        <rect class="gs" x="36" y="40" width="44" height="32" rx="2" stroke-width="4"/>
        <rect class="g" x="26" y="74" width="66" height="5" rx="2"/>
        <rect class="g" x="70" y="44" width="24" height="34" rx="3"/><rect class="disc" x="73" y="48" width="18" height="26"/>
        <rect class="g" x="62" y="58" width="12" height="22" rx="2"/><rect class="disc" x="64" y="61" width="8" height="15"/>
      </svg>
      <p>GUI supports access<br>from many devices</p>
    </div>
  </section>

  <section class="panel panel--agents">
    <div class="badge" style="left:357px;top:8px">
      <svg viewBox="0 0 120 120"><circle class="disc" cx="60" cy="60" r="60"/>
        <polygon class="shade" clip-path="url(#disc-clip)" points="80,30 140,90 140,140 60,140 34,110"/>
        <circle class="gs" cx="66" cy="44" r="18" stroke-width="5"/>
        <rect class="g" x="60" y="32" width="12" height="24" rx="1"/>
        <g class="gs-blue" stroke-width="1.5"><line x1="62" y1="37" x2="70" y2="37"/><line x1="62" y1="41" x2="70" y2="41"/><line x1="62" y1="45" x2="70" y2="45"/></g>
        <line class="gs" x1="52" y1="58" x2="34" y2="78" stroke-width="9"/>
      </svg>
    </div>
    <h2 class="section-title" style="top:128px">MONITORING AGENTS</h2>
    <div class="badge" style="left:66px;top:170px">
      <svg viewBox="0 0 120 120"><circle class="disc" cx="60" cy="60" r="60"/>
        <polygon class="shade" clip-path="url(#disc-clip)" points="90,40 140,90 140,140 80,140 30,90"/>
        <text x="60" y="58" text-anchor="middle" font-size="19">Relayix</text>
        <text x="60" y="78" text-anchor="middle" font-size="16">Server</text></svg>
    </div>
    <div class="badge" style="left:260px;top:170px">
      <svg viewBox="0 0 120 120"><circle class="disc" cx="60" cy="60" r="60"/>
        <polygon class="shade" clip-path="url(#disc-clip)" points="90,40 140,90 140,140 80,140 30,90"/>
        <text x="60" y="58" text-anchor="middle" font-size="19">Quarrydb</text>
        <text x="60" y="78" text-anchor="middle" font-size="16">Server</text></svg>
    </div>
    <div class="badge" style="left:456px;top:170px">
      <svg viewBox="0 0 120 120"><circle class="disc" cx="60" cy="60" r="60"/>
        <polygon class="shade" clip-path="url(#disc-clip)" points="90,40 140,90 140,140 80,140 30,90"/>
        <text x="60" y="58" text-anchor="middle" font-size="19">Panelo</text>
        <text x="60" y="78" text-anchor="middle" font-size="16">Server</text></svg>
    </div>
    <div class="badge" style="left:650px;top:170px">
      <svg viewBox="0 0 120 120"><circle class="disc" cx="60" cy="60" r="60"/>
        <polygon class="shade" clip-path="url(#disc-clip)" points="92,50 140,98 140,140 84,140 36,92"/>
        <circle class="gs" cx="60" cy="24" r="6" stroke="#f5a623" stroke-width="3"/>
        <rect class="acc" x="51" y="33" width="18" height="3" rx="1"/><rect class="acc" x="51" y="39" width="18" height="3" rx="1"/>
        <polygon class="g" points="38,58 60,66 82,58 82,84 60,96 38,84"/>
        <polygon class="g" points="38,58 28,48 50,40 60,50"/>
        <polygon class="g" points="82,58 92,48 70,40 60,50"/>
        <polyline class="gs-blue" stroke-width="2" points="38,58 60,66 82,58"/>
        <line class="gs-blue" stroke-width="2" x1="60" y1="66" x2="60" y2="96"/>
      </svg>
    </div>
  </section>

  <section class="panel panel--plugins">
    <div class="badge" style="left:356px;top:1px">
      <svg viewBox="0 0 120 120"><circle class="disc" cx="60" cy="60" r="60"/>
        <polygon class="shade" clip-path="url(#disc-clip)" points="70,25 95,45 140,90 140,140 60,140 40,95"/>
        <g transform="rotate(45 75 40)"><rect class="g" x="66" y="22" width="18" height="26" rx="2"/><rect class="g" x="70" y="48" width="10" height="14"/>
        <g class="disc"><rect x="69" y="26" width="2" height="8"/><rect x="73" y="26" width="2" height="8"/><rect x="77" y="26" width="2" height="8"/></g></g>
        <path class="gs" stroke-width="5" d="M58,58 C40,70 34,86 46,92 C54,96 62,94 66,90"/>
      </svg>
    </div>
    <h2 class="section-title" style="top:121px">PLUGINS</h2>
    <div class="badge badge--ringed" style="left:57px;top:140px">
      <svg viewBox="0 0 126 126"><circle class="ring" cx="63" cy="63" r="62"/><circle class="disc-deep" cx="63" cy="63" r="55"/>
        <circle class="gs" cx="40" cy="46" r="4.5" stroke="#f5a623" stroke-width="2.5"/><rect class="acc" x="34" y="54" width="12" height="3"/><rect class="acc" x="34" y="59" width="12" height="3"/>
        <text x="74" y="62" text-anchor="middle" font-size="20">+ {•••}</text>
        <text x="63" y="89" text-anchor="middle" font-size="19">APIs</text></svg>
    </div>
    <div class="badge badge--ringed" style="left:251px;top:140px">
      <svg viewBox="0 0 126 126"><circle class="ring" cx="63" cy="63" r="62"/><circle class="disc-deep" cx="63" cy="63" r="55"/>
        <text x="63" y="69" text-anchor="middle" font-size="17">Norvane</text></svg>
    </div>
    <div class="badge badge--ringed" style="left:447px;top:140px">
      <svg viewBox="0 0 126 126"><circle class="ring" cx="63" cy="63" r="62"/><circle class="disc-deep" cx="63" cy="63" r="55"/>
        <text x="63" y="69" text-anchor="middle" font-size="15">Hublane Center</text></svg>
    </div>
    <div class="badge badge--ringed" style="left:643px;top:140px">
      <svg viewBox="0 0 126 126"><circle class="ring" cx="63" cy="63" r="62"/><circle class="disc-deep" cx="63" cy="63" r="55"/>
        <text x="63" y="69" text-anchor="middle" font-size="17">Zipvane</text></svg>
    </div>
  </section>
</div>
</body>
</html>
```